Pilates Classes Flyer Design

I need a flyer designed that will promote my range of classes held in Bath, UK. I teach beginners, intermediate level and Over 50's and 60's and also teach individuals in their own homes. I would like to see designs using my colours blue Pantone 306 and Lime Green 14-0452 TPX TCX. The flyer should reflect a friendly, welcoming and professional class structure. I attach an old flyer for your reference and copy.

Target Market(s)

Men and Women who have busy lives working hard, who recognise they need to stretch out, do some exercise and de-stress after a busy day

Ladies over 50 who want to do some Pilates in a friendly fun environment and meet people at the same time.

Industry/Entity Type

It Professional

Font styles to use
Sans Serif
Script

Requirements
Must have
• One-sided flyer
Text only logo. Drop the figure

```html
<!DOCTYPE html>
<html lang="en">
<head>
<meta charset="utf-8">
<title>FlexLine Pilates – Class Flyer</title>
<link rel="stylesheet" href="https://fonts.googleapis.com/css2?family=Lobster+Two:ital,wght@1,700&family=Oswald:wght@500&family=Roboto:wght@300;400;500;700&display=swap">
<style>
  :root{
    --page:#ecebe8;
    --paper:#ffffff;
    --sky:#a8d9f2;
    --sky-deep:#8ccbeb;
    --lime:#c3d88a;
    --ink:#333a40;
    --ink-soft:#4a5258;
    --band:#a9d8f0;
    --band-text:#2f3b45;
    --brand:#3fa6c8;
    --badge:#2f7f98;
  }
  *{box-sizing:border-box;margin:0;padding:0}
  html,body{width:1200px;height:1084px;overflow:hidden}
  body{background:var(--page);font-family:"Roboto",Arial,sans-serif;color:var(--ink);position:relative}

  .flyer{position:absolute;left:40px;top:170px;width:1120px;height:744px;background:var(--paper);overflow:hidden;box-shadow:0 2px 8px rgba(0,0,0,.12)}
  .flyer__shapes{position:absolute;inset:0}

  .venues{position:absolute;left:42px;top:78px;width:360px;font-size:16px;line-height:1.4;white-space:nowrap}
  .venues__intro{margin-bottom:16px}
  .venue{padding-bottom:10px;margin-bottom:10px;border-bottom:2px dotted var(--ink-soft)}
  .venue:last-child{border-bottom:none}
  .venue__name{font-weight:700}

  .brand-name{font-weight:300;color:var(--brand);letter-spacing:1px;white-space:nowrap}
  .brand-name--left{position:absolute;left:42px;top:400px;font-size:40px;color:#ffffff}

  .contact{position:absolute;left:30px;top:560px;width:330px;text-align:center}
  .contact__call{font-size:20px}
  .contact__phone{font-size:38px;font-weight:500;margin:4px 0}
  .contact__email{font-size:19px}

  .headline{position:absolute;left:500px;right:20px;top:70px;text-align:center;font-family:"Lobster Two",cursive;font-style:italic;font-weight:700;font-size:120px;line-height:1;color:#3b3b3b}
  .intro{position:absolute;left:500px;right:20px;top:210px;text-align:center;font-size:20px;line-height:1.3;color:var(--ink-soft)}

  .band{position:absolute;left:450px;right:0;top:316px;height:54px;background:var(--band);display:flex;align-items:center;justify-content:center}
  .band::before,.band::after{content:"";position:absolute;left:0;right:0;border-top:2px dashed #ffffff}
  .band::before{top:5px}.band::after{bottom:5px}
  .band__text{font-family:"Oswald",sans-serif;font-weight:500;font-size:32px;letter-spacing:2px;color:var(--band-text)}

  .features{position:absolute;left:470px;top:420px;list-style:none;font-size:19px;white-space:nowrap}
  .features__item{display:flex;align-items:center;gap:14px;height:36px}
  .features__item--strong{font-weight:700}
  .features__icon{width:18px;height:18px;flex:none}

  .brand-name--footer{position:absolute;left:520px;top:604px;font-size:30px;display:flex;align-items:center;gap:10px}
  .brand-name__dot{width:14px;height:14px;border-radius:50%;background:var(--lime)}
  .badge{position:absolute;left:840px;top:640px;width:196px;height:60px;border-radius:6px;background:var(--badge)}
</style>
</head>
<body>
<main class="flyer">
  <svg class="flyer__shapes" viewBox="0 0 1120 744" width="1120" height="744" aria-hidden="true">
    <path d="M0 0H482C430 200 350 330 410 480C450 600 520 680 570 744H0Z" fill="var(--lime)"/>
    <path d="M0 0H462C412 200 332 330 392 480C432 600 500 680 548 744H0Z" fill="#ffffff"/>
    <defs>
      <linearGradient id="panelFill" x1="0" y1="0" x2="0" y2="1">
        <stop offset="0" stop-color="var(--sky)"/>
        <stop offset="1" stop-color="var(--sky-deep)"/>
      </linearGradient>
    </defs>
    <path d="M0 0H452C402 200 322 330 382 480C422 600 490 680 536 744H0Z" fill="url(#panelFill)"/>
  </svg>

  <section class="venues">
    <p class="venues__intro">Join my one-hour classe at:</p>
    <div class="venue"><p class="venue__name">St. Anne's Church Hall, Elm Rise</p><p>Monday evenings - Tuesday &amp; Friday mornings</p></div>
    <div class="venue"><p class="venue__name">Willow Meadows Surgery</p><p>Tuesday evenings</p></div>
    <div class="venue"><p class="venue__name">Hartley Centre, Mill Road</p><p>Wednesday mornings &amp; evenings</p></div>
  </section>

  <p class="brand-name brand-name--left">FlexLine Pilates</p>

  <section class="contact">
    <p class="contact__call">Call Nadia Now</p>
    <p class="contact__phone">07700900457</p>
    <p class="contact__email">nadia.fairweather@mailbox.co.uk</p>
  </section>

  <h1 class="headline">Pilates</h1>
  <p class="intro">Pilates is for EVERYONE whatever level of fitnes,<br>age or ability to help you buid strength, flexibility<br>and overall well-being</p>

  <div class="band"><span class="band__text">NEW CLASSES NEAR YOU!</span></div>

  <ul class="features">
    <li class="features__item"><svg class="features__icon" viewBox="0 0 18 18"><rect x="1" y="3" width="13" height="13" fill="none" stroke="#333" stroke-width="1.6"/><path d="M4 9l4 4 9-11" fill="none" stroke="#333" stroke-width="2"/></svg>Quality teaching with Balanced Motion Method Teacher</li>
    <li class="features__item features__item--strong"><svg class="features__icon" viewBox="0 0 18 18"><rect x="1" y="3" width="13" height="13" fill="none" stroke="#333" stroke-width="1.6"/><path d="M4 9l4 4 9-11" fill="none" stroke="#333" stroke-width="2"/></svg>Progressive approach. Teaching good movement</li>
    <li class="features__item"><svg class="features__icon" viewBox="0 0 18 18"><rect x="1" y="3" width="13" height="13" fill="none" stroke="#333" stroke-width="1.6"/><path d="M4 9l4 4 9-11" fill="none" stroke="#333" stroke-width="2"/></svg>Small class sizes and friendly atmosphere</li>
    <li class="features__item features__item--strong"><svg class="features__icon" viewBox="0 0 18 18"><rect x="1" y="3" width="13" height="13" fill="none" stroke="#333" stroke-width="1.6"/><path d="M4 9l4 4 9-11" fill="none" stroke="#333" stroke-width="2"/></svg>Beginners, Intermediate and Over 50's classes to choose</li>
  </ul>

  <p class="brand-name brand-name--footer"><span class="brand-name__dot"></span>FlexLine Pilates</p>
  <div class="badge" role="img" aria-label="Teacher certification badge"></div>
</main>
</body>
</html>
```